Gym Menu

Hi,

I would like to create a menu for my fitness center/ Dance school.

I do have a picture of how i would like it to look like ill attach it down there and instead of the Mexican looking icons i would like to have gym related icons example (Bar bell, dumbbells, etc..)

The menu will consist of the following

Smoothies
- Lagoon Waltz (20 SR)
(Kiwi, Pineapple, Banana, Grapes)
-Coral Drift (20 SR)
(Orange, Peach, Pineapple)
-Tidy Kick (20 SR)
(Carrot, Mango, Orange)
-Purple Thunder (20 SR)
(Blackberry, Raspberry, Banana)
-Cool Breeze (20 SR)
( Lemonade, Mint)
-Ruby Lantern (20 SR)
(Lemonade, Strawberry, Mint)

Mean Green Juices

-Quick Sprout (20SR)
(Cucumber, Celery, Green Apple, Spinach, Lemon, Ginger)
-Hop To It Now! (20 SR)
(Carrots, Apple, Beetroot)

Shake It Up

-Dusky Swirl (20 SR)
(Mocha, Skimmed Milk)

- Velvet Tumbler
(Chocolate, Skimmed Milk)

-Big Lift Zest

(Peanut Butter, Honey, Skimmed Milk, Banana) (20 SR)

Yummy Bites

- Zataar Croissant (10 SR)
- Cheese Croissant (10 SR)
- Plane Croissant (10 SR)
- Blueberry Muffin (7 SR)
- Chocolate Muffin (7 SR)
- Vanilla Muffin (7SR)
- Cookies (7 SR)
- Brownie (10 SR)
-Fresh Berry Popsicle (10 SR)
- Fresh Orange Popsicle (10 SR)

Make it Lite

-Garden Salad (15 SR)
-Greek Salad (15 SR)
-Ceaser Salad (15 SR)
-Italian Salad (15 SR)
- Tuna Sandwich (25 SR)
- Turkey Sandwich (25 SR)
- Chicken Sandwich (25 SR)
-Happy Patch Bowls (8SR)
- Mixed Nuts (10 SR)

Coffee and tea
- Americano (10 SR)
- Espresso (10 SR)
- Turkish Coffee (10 SR)
- Cappuccino (15 SR)
- Cafe Latte (15 SR)
-Hot Cacao (15 SR)
-Extra shor + 5SR

- Green Tea (10 SR)
- Earl Grey (10 SR)
- English Breakfast (10SR)

• The gyms color is orange ... i want this to be in the menu

the gyms name is vartomel i also want this in big somewhere

Colors of the menu should be

Orange
Yellow
green
red

all shades

```html
<!DOCTYPE html>
<html lang="en">
<head>
<meta charset="UTF-8">
<title>Vartomel Menu</title>
<link href="https://fonts.googleapis.com/css2?family=Baloo+2:wght@800&family=Signika:wght@500;600&display=swap" rel="stylesheet">
<style>
  :root {
    --orange: #f28c0f;
    --orange-soft: #f7a33a;
    --green: #1d6a2c;
    --white: #ffffff;
    --yellow: #ffe14d;
    --stage: #d6d6d6;
  }
  * { margin: 0; padding: 0; box-sizing: border-box; }
  html, body { width: 1200px; height: 1000px; overflow: hidden; }
  body { background: var(--stage); font-family: 'Signika', sans-serif; position: relative; }

  .sheet {
    position: absolute; left: 30px; width: 1140px; overflow: hidden;
    background:
      radial-gradient(ellipse at 30% 40%, var(--orange-soft) 0%, transparent 45%),
      radial-gradient(ellipse at 75% 70%, var(--orange-soft) 0%, transparent 40%),
      var(--orange);
  }
  .inner-spread { top: 16px; height: 640px; }
  .back-cover { top: 672px; height: 312px; }

  .fold-line { position: absolute; left: 570px; top: 0; width: 1px; height: 100%; background: rgba(255,255,255,.35); }

  .barbell-art {
    position: absolute; left: 320px; top: 60px; width: 230px; height: 200px;
    background: linear-gradient(135deg, rgba(255,255,255,.55), rgba(255,255,255,.25));
    border-radius: 30px;
  }

  .header-bar { position: absolute; background: var(--white); border-radius: 30px; }
  .bar-juices { left: 0; top: 300px; width: 420px; height: 32px; border-radius: 0 18px 18px 0; }
  .bar-shake { left: 70px; top: 430px; width: 220px; height: 44px; }
  .bar-lite { left: 580px; top: 290px; width: 200px; height: 38px; }
  .bar-coffee { left: 860px; top: 318px; width: 280px; height: 52px; border-radius: 30px 0 0 30px; }

  .section-title {
    position: absolute; font-family: 'Baloo 2', sans-serif; font-weight: 800; color: var(--green);
    line-height: 1; white-space: nowrap;
    text-shadow: 2px 2px 0 var(--white), -2px -2px 0 var(--white), 2px -2px 0 var(--white), -2px 2px 0 var(--white);
  }

  .item-list { position: absolute; list-style: none; color: var(--white); white-space: nowrap; }
  .item-list li { font-weight: 600; }
  .item-list .ingredients { display: block; color: var(--yellow); font-weight: 500; font-size: 11px; line-height: 13px; margin-bottom: 4px; }

  .smoothies-title { left: 30px; top: 14px; font-size: 34px; }
  .smoothies-list { left: 40px; top: 60px; font-size: 16px; line-height: 19px; }

  .juices-title { left: 36px; top: 302px; font-size: 28px; }
  .juices-list { left: 40px; top: 344px; font-size: 16px; line-height: 19px; }

  .shake-title { left: 86px; top: 438px; font-size: 28px; }
  .shake-list { left: 40px; top: 490px; font-size: 16px; line-height: 19px; }

  .brand-name {
    position: absolute; font-family: 'Signika', sans-serif; font-weight: 600;
    color: var(--white); line-height: 1; white-space: nowrap;
  }
  .inner-spread .brand-name { left: 310px; top: 490px; font-size: 96px; }

  .bites-title { left: 700px; top: 14px; font-size: 34px; }
  .bites-list { left: 706px; top: 60px; font-size: 16px; line-height: 21px; }

  .lite-title { left: 594px; top: 296px; font-size: 26px; }
  .lite-list { left: 594px; top: 338px; font-size: 12px; line-height: 15px; }

  .coffee-title { left: 880px; top: 328px; font-size: 30px; }
  .coffee-list { left: 880px; top: 386px; font-size: 16px; line-height: 20px; }
  .coffee-list .gap { margin-top: 16px; }

  .back-lite-title { left: 30px; top: 28px; font-size: 42px; }
  .back-shake-title { left: 40px; top: 100px; font-size: 30px; }
  .back-bites-title { left: 30px; top: 240px; font-size: 42px; }
  .bowl-art {
    position: absolute; left: 340px; top: 40px; width: 300px; height: 230px;
    background: linear-gradient(160deg, rgba(255,255,255,.85), rgba(255,255,255,.55));
    border-radius: 40px 40px 150px 150px;
  }
  .faint-word {
    position: absolute; font-family: 'Baloo 2', sans-serif; font-weight: 800;
    color: rgba(255,255,255,.45); line-height: 1; white-space: nowrap;
  }
  .fw-croissant { left: 680px; top: 18px; font-size: 26px; }
  .fw-fresh { left: 700px; top: 46px; font-size: 44px; }
  .fw-chocolate { left: 860px; top: 60px; font-size: 26px; }
  .fw-salad { left: 690px; top: 104px; font-size: 26px; }
  .back-cover .brand-name { left: 670px; top: 150px; font-size: 110px; }
</style>
</head>
<body>
  <main class="sheet inner-spread">
    <div class="barbell-art" role="img" aria-label="Large barbell illustration"></div>
    <div class="fold-line"></div>

    <div class="header-bar bar-juices"></div>
    <div class="header-bar bar-shake"></div>
    <div class="header-bar bar-lite"></div>
    <div class="header-bar bar-coffee"></div>

    <h2 class="section-title smoothies-title">Smoothies</h2>
    <ul class="item-list smoothies-list">
      <li>Lagoon Waltz (20 SR)<span class="ingredients">(Kiwi, Pineapple, Banana, Grapes)</span></li>
      <li>Coral Drift (20 SR)<span class="ingredients">(Orange, Peach, Pineapple)</span></li>
      <li>Tidy Kick (20 SR)<span class="ingredients">(Carrot, Mango, Orange)</span></li>
      <li>Purple Thunder (20 SR)<span class="ingredients">(Blackberry, Raspberry, Banana)</span></li>
      <li>Cool Breeze (20 SR)<span class="ingredients">( Lemonade, Mint)</span></li>
      <li>Ruby Lantern (20 SR)<span class="ingredients">(Lemonade, Strawberry, Mint)</span></li>
    </ul>

    <h2 class="section-title juices-title">Mean Green Juices</h2>
    <ul class="item-list juices-list">
      <li>Quick Sprout (20SR)<span class="ingredients">(Cucumber, Celery, Green Apple, Spinach, Lemon, Ginger)</span></li>
      <li>Hop To It Now! (20 SR)<span class="ingredients">(Carrots, Apple, Beetroot)</span></li>
    </ul>

    <h2 class="section-title shake-title">Shake It Up</h2>
    <ul class="item-list shake-list">
      <li>Dusky Swirl (20 SR)<span class="ingredients">(Mocha, Skimmed Milk)</span></li>
      <li>Velvet Tumbler<span class="ingredients">(Chocolate, Skimmed Milk)</span></li>
      <li>Big Lift Zest<span class="ingredients">(Peanut Butter, Honey, Skimmed Milk, Banana) (20 SR)</span></li>
    </ul>

    <div class="brand-name">vartomel</div>

    <h2 class="section-title bites-title">Yummy Bites</h2>
    <ul class="item-list bites-list">
      <li>Zataar Croissant (10 SR)</li>
      <li>Cheese Croissant (10 SR)</li>
      <li>Plane Croissant (10 SR)</li>
      <li>Blueberry Muffin (7 SR)</li>
      <li>Chocolate Muffin (7 SR)</li>
      <li>Vanilla Muffin (7SR)</li>
      <li>Cookies (7 SR)</li>
      <li>Brownie (10 SR)</li>
      <li>Fresh Berry Popsicle (10 SR)</li>
      <li>Fresh Orange Popsicle (10 SR)</li>
    </ul>

    <h2 class="section-title lite-title">Make it Lite</h2>
    <ul class="item-list lite-list">
      <li>Garden Salad (15 SR)</li>
      <li>Greek Salad (15 SR)</li>
      <li>Ceaser Salad (15 SR)</li>
      <li>Italian Salad (15 SR)</li>
      <li>Tuna Sandwich (25 SR)</li>
      <li>Turkey Sandwich (25 SR)</li>
      <li>Chicken Sandwich (25 SR)</li>
      <li>Happy Patch Bowls (8SR)</li>
      <li>Mixed Nuts (10 SR)</li>
    </ul>

    <h2 class="section-title coffee-title">Coffee and tea</h2>
    <ul class="item-list coffee-list">
      <li>Americano (10 SR)</li>
      <li>Espresso (10 SR)</li>
      <li>Turkish Coffee (10 SR)</li>
      <li>Cappuccino (15 SR)</li>
      <li>Cafe Latte (15 SR)</li>
      <li>Hot Cacao (15 SR)</li>
      <li>Extra shor + 5SR</li>
      <li class="gap">Green Tea (10 SR)</li>
      <li>Earl Grey (10 SR)</li>
      <li>English Breakfast (10SR)</li>
    </ul>
  </main>

  <section class="sheet back-cover">
    <h2 class="section-title back-lite-title">Make it Lite</h2>
    <h2 class="section-title back-shake-title">Shake It Up</h2>
    <div class="bowl-art" role="img" aria-label="Salad bowl illustration"></div>
    <span class="faint-word fw-croissant">Croissant</span>
    <span class="faint-word fw-fresh">Fresh</span>
    <span class="faint-word fw-chocolate">Chocolate</span>
    <span class="faint-word fw-salad">Salad</span>
    <div class="brand-name">vartomel</div>
    <h2 class="section-title back-bites-title">Yummy Bites</h2>
  </section>
</body>
</html>
```